letterhead design

can you create a letterhead using the logo you created and the following:

318 W Dunhaven Elgin IL 60123
(p) 847-555-0143
(f) 847-555-0178
www.thebrantleylawgroup.com

Industry/Entity Type

Law

Requirements
Must have
• Use logo attached: must have address 318 W Dunhaven Elgin IL 60123 phone 847-555-0143 fax 847-555-0178
Should not have
• Nothing other thank logo and address/phone/website

```html
<!DOCTYPE html>
<html lang="en">
<head>
<meta charset="utf-8">
<title>Brantley Law Group — Letterhead</title>
<link href="https://fonts.googleapis.com/css2?family=Cinzel:wght@400&family=Prata&display=swap" rel="stylesheet">
<style>
  :root {
    --backdrop: #3d3d3d;
    --paper: #ffffff;
    --ink: #050709;
    --gold: #e4b55c;
    --gold-soft: rgba(228, 181, 92, 0.28);
    --watermark: #efefef;
    --footer-text: #f4f1ea;
  }
  * { box-sizing: border-box; margin: 0; padding: 0; }
  html, body {
    width: 1200px;
    height: 1200px;
    overflow: hidden;
    background: var(--backdrop);
  }
  .letterhead {
    position: absolute;
    left: 242px;
    top: 93px;
    width: 716px;
    height: 1014px;
    background: var(--paper);
    overflow: hidden;
  }
  .header-art, .footer-art, .watermark {
    position: absolute;
    left: 0;
    top: 0;
  }
  .header-wave {
    position: absolute;
    left: 162px;
    top: 0;
    width: 554px;
    height: 146px;
    background: linear-gradient(100deg, rgba(5,7,9,0) 0%, var(--gold-soft) 45%, rgba(5,7,9,0) 70%, var(--gold-soft) 100%);
    opacity: 0.45;
  }
  .brand {
    position: absolute;
    left: 20px;
    top: 106px;
    width: 254px;
    text-align: center;
    font-family: "Cinzel", serif;
    font-weight: 400;
    color: var(--gold);
  }
  .brand-name {
    display: block;
    font-size: 23px;
    letter-spacing: 0.5px;
    line-height: 1;
  }
  .brand-sub {
    display: block;
    font-size: 12.5px;
    letter-spacing: 1.5px;
    margin-top: 7px;
  }
  .footer-wave {
    position: absolute;
    left: 441px;
    top: 884px;
    width: 275px;
    height: 77px;
    background: linear-gradient(100deg, rgba(5,7,9,0) 0%, var(--gold-soft) 60%, rgba(5,7,9,0) 100%);
    opacity: 0.5;
  }
  .contact {
    position: absolute;
    font-family: "Prata", serif;
    font-size: 13px;
    color: var(--footer-text);
    display: flex;
    align-items: center;
    gap: 9px;
    white-space: nowrap;
  }
  .contact svg { width: 17px; height: 17px; flex: none; }
  .contact-phone { left: 231px; top: 898px; }
  .contact-fax { left: 360px; top: 898px; }
  .contact-web { left: 229px; top: 926px; }
  .contact-address { left: 454px; top: 924px; }
</style>
</head>
<body>
  <main class="letterhead">
    <svg class="header-art" width="716" height="210" viewBox="0 0 716 210">
      <circle cx="166" cy="46" r="153" fill="var(--gold)"/>
      <rect x="0" y="0" width="716" height="152" fill="var(--gold)"/>
      <rect x="0" y="0" width="716" height="146" fill="var(--ink)"/>
      <circle cx="150" cy="39.5" r="153" fill="var(--ink)"/>
      <circle cx="147" cy="67" r="35" fill="none" stroke="var(--gold)" stroke-width="2"/>
    </svg>
    <div class="header-wave" role="img" aria-label="Flowing gold line-wave decoration"></div>
    <div class="brand">
      <span class="brand-name">BRANTLEY LAW</span>
      <span class="brand-sub">GROUP</span>
    </div>

    <svg class="watermark" width="716" height="800" viewBox="0 0 716 800" aria-hidden="true">
      <circle cx="378" cy="499" r="180" fill="none" stroke="var(--watermark)" stroke-width="9"/>
    </svg>

    <svg class="footer-art" width="716" height="1014" viewBox="0 0 716 1014">
      <rect x="0" y="880" width="716" height="84" fill="var(--gold)"/>
      <rect x="0" y="884" width="716" height="77" fill="var(--ink)"/>
      <rect x="0" y="880" width="130" height="84" fill="var(--paper)"/>
      <circle cx="122" cy="908" r="82" fill="var(--ink)" stroke="var(--gold)" stroke-width="4.5"/>
    </svg>
    <div class="footer-wave" role="img" aria-label="Flowing gold line-wave decoration"></div>

    <div class="contact contact-phone">
      <svg viewBox="0 0 24 24"><path fill="var(--gold)" d="M2 9c0-3 5-5 10-5s10 2 10 5v2h-5V9H7v2H2zM6 12h12l2 8H4z"/></svg>
      <span>847-555-0143</span>
    </div>
    <div class="contact contact-fax">
      <svg viewBox="0 0 24 24"><path fill="var(--gold)" d="M3 8h3v13H3zM8 8h13v13H8zM10 2h8v5h-8zM10 14h2v2h-2zm4 0h2v2h-2zm4 0h2v2h-2zm-8 4h2v2h-2zm4 0h2v2h-2zm4 0h2v2h-2z"/></svg>
      <span>847-555-0178</span>
    </div>
    <div class="contact contact-web">
      <svg viewBox="0 0 24 24"><circle cx="12" cy="12" r="9" fill="none" stroke="var(--gold)" stroke-width="2"/><path fill="none" stroke="var(--gold)" stroke-width="1.5" d="M3 12h18M12 3c-4 4-4 14 0 18M12 3c4 4 4 14 0 18"/></svg>
      <span>www.thebrantleylawgroup.com</span>
    </div>
    <div class="contact contact-address">
      <svg viewBox="0 0 24 24"><path fill="var(--gold)" d="M12 1a7 7 0 0 0-7 7c0 5 7 12 7 12s7-7 7-12a7 7 0 0 0-7-7zm0 4.5a2.5 2.5 0 1 1 0 5 2.5 2.5 0 0 1 0-5zM8 22h8v1H8z"/></svg>
      <span>318 w dunhaven elgin il 60123</span>
    </div>
  </main>
</body>
</html>
```